brixtane motor oil

I would like to inform you that our new motor oil brand brixtane will be divided into three categories:
Brixtane high performance Full Synthetic
0w20 ,5w30 ,0w16,5w20
with massage.
Maximum Protection, Ultimate Performance.brixtane quendor
--------------------------------
brixtane quendor Synthetic Blend
10w40,5w30,5w20
with massage
The perfect combination of durability and efficiency
-------------------------------
brixtane gelvoria transmission fluid
ATF III
with massage
proven to maximize transmission life

```html
<!DOCTYPE html>
<html lang="en">
<head>
<meta charset="utf-8">
<title>Brixtane High Performance – Label Sizes</title>
<link rel="stylesheet" href="https://fonts.googleapis.com/css2?family=Titan+One&family=Oswald:wght@500;700&family=Roboto:wght@500&display=swap">
<style>
  :root {
    --paper: #ffffff;
    --frame: #c8c8c8;
    --ink: #111111;
    --label-yellow: #ffe600;
    --label-amber: #f5a300;
    --ribbon-red: #a81c22;
    --wave-maroon: #5e0c10;
    --wave-orange: #f08c1a;
    --pill-grey: #4a4a4a;
    --white: #ffffff;
  }
  * { box-sizing: border-box; margin: 0; padding: 0; }
  html, body {
    width: 1200px; height: 1000px; overflow: hidden;
    background: var(--paper);
  }
  .sheet { position: relative; width: 1200px; height: 1000px; }
  .dimensions { position: absolute; inset: 0; }
  .dim-text {
    font-family: "Roboto", sans-serif; font-weight: 500; font-size: 15px;
    fill: var(--ink); stroke: var(--paper); stroke-width: 8px; paint-order: stroke;
  }

  /* Every label element is placed in em units so all three sizes share one layout */
  .label {
    position: absolute; overflow: hidden;
    border-radius: 2px;
  }
  .label > * { position: absolute; white-space: nowrap; }
  .label-pattern {
    inset: 0;
    background: radial-gradient(ellipse at 50% 45%, var(--label-yellow) 35%, var(--label-amber) 100%);
  }
  .label-brand {
    top: 0.8em; left: 0; right: 0; text-align: center;
    font-family: "Oswald", sans-serif; font-weight: 700;
    font-size: 1.2em; line-height: 1.2; letter-spacing: .03em; color: var(--ink);
    text-transform: uppercase;
  }
  .label-brand .brand-dot {
    display: inline-block; width: .42em; height: .42em; border-radius: 50%;
    background: var(--ink); margin-right: .3em; vertical-align: .18em;
  }
  .label-high {
    top: 0.85em; left: 0; right: 0; text-align: center;
    font-family: "Titan One", sans-serif; font-size: 2.9em; line-height: 1;
    color: var(--ink);
  }
  .label-performance {
    top: 5.75em; left: 0; right: 0; text-align: center;
    font-family: "Titan One", sans-serif; font-size: 1.05em; line-height: 1;
    color: var(--ink); letter-spacing: .02em;
  }
  .label-ribbon {
    top: 7.25em; left: 30%; right: 0; height: 1.45em;
    background: var(--ribbon-red);
    border-radius: .7em 0 0 .7em;
    display: flex; align-items: center; justify-content: center;
    font-family: "Oswald", sans-serif; font-weight: 700; font-size: 1em; line-height: 1;
    color: var(--white); letter-spacing: .03em;
  }
  .label-pill {
    top: 9.05em; left: 2.7em; right: 0.5em; height: 1.75em;
    background: var(--pill-grey); border-radius: 0 .8em .8em 0;
    display: flex; align-items: center; justify-content: center; text-align: center;
    padding-left: .5em;
  }
  .label-pill span {
    font-family: "Oswald", sans-serif; font-weight: 500; font-size: .42em; line-height: 1.35;
    color: var(--white); letter-spacing: .04em; text-transform: uppercase;
  }
  .label-grade {
    top: 8.75em; left: 0.5em; width: 2.4em; height: 2.4em;
    border-radius: 50%; background: var(--ink); border: .15em solid var(--white);
    display: flex; align-items: center; justify-content: center;
  }
  .label-grade span {
    font-family: "Oswald", sans-serif; font-weight: 700; font-size: .85em; line-height: 1;
    color: var(--white);
  }
  .label-wave { left: 0; right: 0; bottom: 0; height: 2.3em; width: 100%; }
  .label-volume {
    right: 0.6em; bottom: 0.35em;
    font-family: "Oswald", sans-serif; font-weight: 700; font-size: 1.15em; line-height: 1;
    color: var(--white);
  }
</style>
</head>
<body>
<main class="sheet">

  <svg class="dimensions" width="1200" height="1000" viewBox="0 0 1200 1000" aria-hidden="true">
    <defs>
      <marker id="arrow" viewBox="0 0 10 10" refX="9" refY="5" markerWidth="7" markerHeight="7" orient="auto-start-reverse">
        <path d="M0 2 L10 5 L0 8 Z" fill="#111"/>
      </marker>
    </defs>
    <rect x="60" y="245" width="1005" height="525" fill="none" stroke="var(--frame)" stroke-width="1"/>
    <g stroke="#111" stroke-width="1" marker-start="url(#arrow)" marker-end="url(#arrow)">
      <line x1="118" y1="402" x2="118" y2="660"/>
      <line x1="400" y1="354" x2="400" y2="660"/>
      <line x1="150" y1="700" x2="362" y2="700"/>
      <line x1="498" y1="441" x2="498" y2="660"/>
      <line x1="770" y1="394" x2="770" y2="660"/>
      <line x1="530" y1="700" x2="733" y2="700"/>
      <line x1="868" y1="498" x2="868" y2="660"/>
      <line x1="1075" y1="466" x2="1075" y2="660"/>
      <line x1="900" y1="700" x2="1039" y2="700"/>
    </g>
    <g class="dim-labels" text-anchor="middle">
      <text class="dim-text" x="118" y="536">171.67</text>
      <text class="dim-text" x="400" y="512">204.18</text>
      <text class="dim-text" x="256" y="705">141.43</text>
      <text class="dim-text" x="498" y="555">146.21</text>
      <text class="dim-text" x="770" y="532">177.35</text>
      <text class="dim-text" x="631" y="705">135.45</text>
      <text class="dim-text" x="868" y="584">108.20</text>
      <text class="dim-text" x="1075" y="568">129.63</text>
      <text class="dim-text" x="969" y="705">92.58</text>
    </g>
  </svg>

  <section class="label label-large" style="left:150px; top:402px; width:212px; height:258px; font-size:21px;">
    <div class="label-pattern" role="img" aria-label="Yellow and amber honeycomb pattern background"></div>
    <div class="label-brand"><span class="brand-dot"></span>Brixtane</div>
    <div class="label-high">high</div>
    <div class="label-performance">performance</div>
    <div class="label-ribbon">FULL SYNTHETIC</div>
    <div class="label-pill"><span>The perfect combination of<br>durability and efficiency</span></div>
    <div class="label-grade"><span>5W30</span></div>
    <svg class="label-wave" viewBox="0 0 100 40" preserveAspectRatio="none" aria-hidden="true">
      <path d="M0 22 C25 34 45 28 65 16 C80 7 92 6 100 8 L100 40 L0 40 Z" fill="var(--wave-maroon)"/>
      <path d="M0 22 C25 34 45 28 65 16 C80 7 92 6 100 8" fill="none" stroke="var(--wave-orange)" stroke-width="3"/>
    </svg>
    <div class="label-volume">1L</div>
  </section>

  <section class="label label-medium" style="left:530px; top:441px; width:203px; height:219px; font-size:18px;">
    <div class="label-pattern" role="img" aria-label="Yellow and amber honeycomb pattern background"></div>
    <div class="label-brand"><span class="brand-dot"></span>Brixtane</div>
    <div class="label-high">high</div>
    <div class="label-performance">performance</div>
    <div class="label-ribbon">FULL SYNTHETIC</div>
    <div class="label-pill"><span>The perfect combination of<br>durability and efficiency</span></div>
    <div class="label-grade"><span>5W30</span></div>
    <svg class="label-wave" viewBox="0 0 100 40" preserveAspectRatio="none" aria-hidden="true">
      <path d="M0 22 C25 34 45 28 65 16 C80 7 92 6 100 8 L100 40 L0 40 Z" fill="var(--wave-maroon)"/>
      <path d="M0 22 C25 34 45 28 65 16 C80 7 92 6 100 8" fill="none" stroke="var(--wave-orange)" stroke-width="3"/>
    </svg>
    <div class="label-volume">1L</div>
  </section>

  <section class="label label-small" style="left:900px; top:498px; width:139px; height:162px; font-size:13px;">
    <div class="label-pattern" role="img" aria-label="Yellow and amber honeycomb pattern background"></div>
    <div class="label-brand"><span class="brand-dot"></span>Brixtane</div>
    <div class="label-high">high</div>
    <div class="label-performance">performance</div>
    <div class="label-ribbon">FULL SYNTHETIC</div>
    <div class="label-pill"><span>The perfect combination of<br>durability and efficiency</span></div>
    <div class="label-grade"><span>5W30</span></div>
    <svg class="label-wave" viewBox="0 0 100 40" preserveAspectRatio="none" aria-hidden="true">
      <path d="M0 22 C25 34 45 28 65 16 C80 7 92 6 100 8 L100 40 L0 40 Z" fill="var(--wave-maroon)"/>
      <path d="M0 22 C25 34 45 28 65 16 C80 7 92 6 100 8" fill="none" stroke="var(--wave-orange)" stroke-width="3"/>
    </svg>
    <div class="label-volume">1L</div>
  </section>

</main>
</body>
</html>
```